Business Card Design

We are a commercial real estate brokerage in San Francisco, leasing office buildings downtown.
I would like a clean, elegant look. Simple but powerful .

Industry/Entity Type

Business

Contact Information for Business Card

Colin Farrow
lic# 07281549
415.555.0172
colin@tarvo-commercial.example
tarvo-commercial.example

```html
<!DOCTYPE html>
<html lang="en">
<head>
<meta charset="utf-8">
<title>Tarvo Commercial – Business Card</title>
<link rel="stylesheet" href="https://fonts.googleapis.com/css2?family=Open+Sans:wght@600;700&display=swap">
<style>
  :root {
    --backdrop: #ecebe8;
    --card: #ffffff;
    --accent: #7787a8;
    --ink: #565656;
    --shadow: rgba(0, 0, 0, 0.18);
  }
  html, body {
    margin: 0;
    width: 1200px;
    height: 1000px;
    overflow: hidden;
    background: var(--backdrop);
    font-family: "Open Sans", Arial, sans-serif;
  }
  .card {
    position: absolute;
    left: 66px;
    top: 192px;
    width: 1069px;
    height: 615px;
    background: var(--card);
    box-shadow: 0 6px 18px var(--shadow);
  }
  .brand {
    position: absolute;
    left: 60px;
    top: 262px;
    display: flex;
    align-items: center;
    gap: 26px;
  }
  .brand-mark {
    width: 64px;
    height: 64px;
    background: var(--accent);
  }
  .brand-name {
    color: var(--accent);
    font-weight: 700;
    line-height: 1;
  }
  .brand-name .primary {
    display: block;
    font-size: 72px;
    letter-spacing: 1px;
  }
  .brand-name .secondary {
    display: block;
    font-size: 30px;
    letter-spacing: 1px;
    margin-top: 2px;
  }
  .divider {
    position: absolute;
    left: 535px;
    top: 108px;
    width: 5px;
    height: 400px;
    background: var(--accent);
  }
  .person {
    position: absolute;
    left: 594px;
    top: 172px;
  }
  .person-name {
    margin: 0;
    font-size: 33px;
    font-weight: 700;
    color: var(--accent);
    letter-spacing: 0.5px;
    line-height: 1.2;
  }
  .license {
    margin: 8px 0 0;
    font-size: 22px;
    font-weight: 700;
    color: var(--ink);
  }
  .contacts {
    position: absolute;
    left: 593px;
    top: 306px;
    margin: 0;
    padding: 0;
    list-style: none;
  }
  .contact {
    display: flex;
    align-items: center;
    gap: 23px;
    height: 32px;
    margin-bottom: 17.5px;
    font-size: 23px;
    font-weight: 700;
    color: var(--ink);
  }
  .contact-icon {
    width: 32px;
    height: 32px;
    flex: none;
  }
</style>
</head>
<body>
  <article class="card">
    <div class="brand">
      <div class="brand-mark"></div>
      <div class="brand-name">
        <span class="primary">TARVO</span>
        <span class="secondary">COMMERCIAL</span>
      </div>
    </div>

    <div class="divider"></div>

    <div class="person">
      <h1 class="person-name">COLIN FARROW</h1>
      <p class="license">lic# 07281549</p>
    </div>

    <ul class="contacts">
      <li class="contact">
        <svg class="contact-icon" viewBox="0 0 32 32" aria-hidden="true">
          <rect width="32" height="32" rx="3" fill="var(--accent)"/>
          <path d="M11 7c1 0 2 3 2.6 4.6.3.9-1.4 1.9-1.4 2.6 0 1.3 3.4 5.9 4.8 6.3.7.2 1.8-1.3 2.6-1 1.6.7 4.3 2.1 4.3 3 0 1.5-2 3.5-3.6 3.5C15 26 6 17 6 11.6 6 9.5 9.4 7 11 7z" fill="#fff"/>
        </svg>
        <span>415.555.0172</span>
      </li>
      <li class="contact">
        <svg class="contact-icon" viewBox="0 0 32 32" aria-hidden="true">
          <rect width="32" height="32" rx="3" fill="var(--accent)"/>
          <rect x="6" y="9" width="20" height="14" fill="#fff"/>
          <path d="M6 9l10 8 10-8M6 23l7.5-7M26 23l-7.5-7" stroke="var(--accent)" stroke-width="1.3" fill="none"/>
        </svg>
        <span>colin@tarvo-commercial.example</span>
      </li>
      <li class="contact">
        <svg class="contact-icon" viewBox="0 0 32 32" aria-hidden="true">
          <rect width="32" height="32" rx="3" fill="var(--accent)"/>
          <g stroke="#fff" stroke-width="1.4" fill="none">
            <circle cx="16" cy="16" r="9"/>
            <ellipse cx="16" cy="16" rx="4" ry="9"/>
            <path d="M7 16h18M8.5 11.5h15M8.5 20.5h15M16 7v18"/>
          </g>
        </svg>
        <span>tarvo-commercial.example</span>
      </li>
    </ul>
  </article>
</body>
</html>
```